My Insurance Agency Show Display

I need to design a 10 ft x 8 ft backdrop for a show display. This is a pop up fabric most likely display that will be used for a show booth. I need someone to design something more attractive with my logo and make it more flashy so people can see and remember my company. I have attached my rough design so far. I would like it to look more modern. The photo in the design does not have to be used.

This is for an insurance agency that provides Home, Auto, Life and Health products to consumers. We also provide Renters insurance, Commercial, RV, mobile homes, and other products to our customers.

Target Market(s)

Home Owners, and Multiple Auto Owners

Industry/Entity Type

Property and Causality Insurance

Font styles to use
Sans Serif

Colors
0054AA
0677BA
7BADD7
CADEEF
E8F1F8
00AB8E
00BBA5
67D7C9
C6EFE9
E9F9F6

Requirements
Must have
• Attractive Modern Layout
Nice to have
• new and creative. Something that pops with color
Should not have
• Any affiliation to other insurance agencies.

```html
<!DOCTYPE html>
<html lang="en">
<head>
<meta charset="UTF-8">
<title>Harbor Insurance Agency – Show Display</title>
<link rel="stylesheet" href="https://fonts.googleapis.com/css2?family=Montserrat:wght@400;500;600;700&family=Open+Sans:wght@400&display=swap">
<style>
  :root {
    --page: #e8f1f8;
    --card: #ffffff;
    --accent: #00ab8e;
    --accent-strong: #0054aa;
    --text: #0b3566;
    --band: #0054aa;
    --phone-bg: #0054aa;
    --photo-light: #cadeef;
    --photo-mid: #7badd7;
    --photo-dark: #0677ba;
    --white: #ffffff;
  }
  * { margin: 0; padding: 0; box-sizing: border-box; }
  html, body {
    width: 1200px; height: 1200px; overflow: hidden;
    background: var(--page);
  }
  .display {
    position: absolute; left: 0; top: 121px;
    width: 1200px; height: 958px;
    background: var(--card);
    overflow: hidden;
  }
  .brand {
    position: absolute; left: 20px; top: 82px; width: 470px;
    display: flex; flex-direction: column; align-items: center;
    font-family: "Montserrat", sans-serif; font-weight: 600;
    color: var(--text); text-align: center;
  }
  .brand-mark {
    width: 80px; height: 80px; background: var(--accent);
    margin-bottom: 54px;
  }
  .brand-name { font-size: 36px; line-height: 1.1; letter-spacing: 0.5px; white-space: nowrap; }
  .brand-sub {
    display: flex; align-items: center; gap: 18px;
    font-size: 28px; letter-spacing: 8px; margin-top: 10px;
  }
  .brand-sub::before, .brand-sub::after {
    content: ""; width: 70px; height: 2px; background: var(--accent);
  }
  .photo {
    position: absolute; left: 511px; top: 0; width: 689px; height: 472px;
    background: linear-gradient(160deg, var(--photo-light) 0%, var(--photo-mid) 50%, var(--photo-dark) 100%);
  }
  .ribbon { position: absolute; left: 0; top: 0; width: 1200px; height: 958px; }
  .services {
    position: absolute; right: 61px; top: 512px;
    font-family: "Montserrat", sans-serif; font-weight: 400;
    font-size: 30px; line-height: 36px; color: var(--white);
    text-align: right; text-transform: uppercase;
  }
  .headline {
    position: absolute; left: 60px; top: 484px;
    font-family: "Montserrat", sans-serif; font-weight: 500;
    font-size: 52px; line-height: 60px; color: var(--text);
    text-transform: uppercase;
  }
  .headline .accent { color: var(--accent); }
  .headline .lead { font-weight: 700; font-size: 57px; }
  .intro {
    position: absolute; left: 60px; top: 700px; width: 725px;
    font-family: "Open Sans", sans-serif; font-size: 22px; line-height: 37px;
    color: var(--text);
  }
  .phone {
    position: absolute; left: 855px; top: 758px; width: 345px; height: 67px;
    background: var(--phone-bg); color: var(--white);
    font-family: "Montserrat", sans-serif; font-weight: 700; font-size: 37px;
    display: flex; align-items: center; justify-content: center; letter-spacing: 1px;
  }
  .footer-band {
    position: absolute; left: 0; bottom: 0; width: 1200px; height: 34px;
    background: var(--band);
  }
</style>
</head>
<body>
  <main class="display">
    <div class="brand">
      <div class="brand-mark"></div>
      <div class="brand-name">HARBOR INSURANCE</div>
      <div class="brand-sub">AGENCY</div>
    </div>

    <div class="photo" role="img" aria-label="Photo of a laughing family of four playing together on a grey sofa in a bright kitchen-living room"></div>

    <svg class="ribbon" viewBox="0 0 1200 958" aria-hidden="true">
      <polygon points="511,472 1200,472 1200,684 855,684" fill="var(--accent)"/>
    </svg>

    <div class="services">
      Home | Auto | Life | Health<br>
      Umbrella | Renters<br>
      Commercial
    </div>

    <h1 class="headline">
      <span class="accent lead">Protecting</span><br>
      What Matters<br>
      Most to <span class="accent">You</span>
    </h1>

    <p class="intro">Our comprehensive insurance services provide you with peace of mind, ensuring that your assets, health, and loved ones are safeguarded against unforeseen circumstances. Trust in our expertise to navigate the complexities of insurance and secure a brighter future for you and your family.</p>

    <div class="phone">555-214-0188</div>

    <div class="footer-band"></div>
  </main>
</body>
</html>
```